Corbant Invitation Template (Editable Canva Design)

We are seeking a clean, professional invitation template for Corbant that aligns with our company branding and colors. The most important requirement is that the design must be created in Canva so that our team can easily edit and reuse it for future events.
The invitation should include the following sections:
Event Blurb: A short paragraph describing the meeting, dinner, or event.
Date & Time: Clearly displayed and easy to read.
Location: With space for venue details.
Closing/Contact Section: A small closing note with instructions on who to reach out to, plus a closing blurb.
Design Requirements:
Must match Corbant company colors
Utitlize both the CORBANT & KELO BRIM TZ logos (Corbant is main and KELO BRIM TZ is secondary)
Professional and polished, while still visually engaging.
Sized appropriately for both email and print sharing.
Delivered as a Canva template (so we can edit text, sections, and reuse easily).
I have attached an example of the template we used in the past that we do NOT like the look of - but you can get an idea of the different sections we need on the invite. Please do not try to make the new invites look anything like our old one.
Target Market(s)
Physicians (Pain Management)
Industry/Entity Type
Medical Device

```html
<!DOCTYPE html>
<html lang="en">
<head>
<meta charset="utf-8">
<title>Corbant Invitation</title>
<link href="https://fonts.googleapis.com/css2?family=Bebas+Neue&family=Poppins:ital,wght@0,400;0,500;0,600;0,700;1,300&display=swap" rel="stylesheet">
<style>
  :root {
    --green: #6cb33f;
    --green-light: #a9c95c;
    --ink: #030503;
    --bg-dark: #0d1905;
    --bg-glow: #3f7d12;
    --white: #ffffff;
    --shadow: #8a8a8a;
  }
  * { margin: 0; padding: 0; box-sizing: border-box; }
  html, body { width: 851px; height: 1200px; overflow: hidden; background: var(--bg-dark); }
  .invitation {
    position: relative;
    width: 851px;
    height: 1200px;
    overflow: hidden;
    font-family: "Poppins", sans-serif;
    color: var(--white);
    background:
      radial-gradient(ellipse 520px 420px at 100% 100%, var(--bg-glow) 0%, rgba(63,125,18,0.35) 45%, rgba(13,25,5,0) 100%),
      linear-gradient(135deg, #0a1304 0%, var(--bg-dark) 55%, #15300a 100%);
  }
  .card {
    position: absolute;
    left: 86px; top: 86px;
    width: 678px; height: 1026px;
    border-radius: 40px;
    padding: 5px;
    background: linear-gradient(90deg, var(--green) 0%, var(--green-light) 100%);
  }
  .card-inner {
    width: 100%; height: 100%;
    border-radius: 35px;
    background: var(--ink);
  }
  .brand {
    position: absolute;
    top: 158px; left: 0; width: 851px;
    text-align: center;
    font-weight: 500;
    font-size: 64px;
    letter-spacing: 2px;
    line-height: 1;
    color: var(--green);
  }
  .headline {
    position: absolute;
    top: 294px; left: 0; width: 851px;
    text-align: center;
    font-family: "Bebas Neue", sans-serif;
    font-weight: 400;
    font-size: 124px;
    line-height: 1;
    letter-spacing: 1px;
    color: var(--white);
    text-shadow: 4px 4px 0 var(--shadow);
  }
  .detail {
    position: absolute;
    display: flex;
    align-items: center;
  }
  .detail svg { flex: none; }
  .detail-date { left: 233px; top: 467px; }
  .detail-time { left: 231px; top: 543px; }
  .detail-place { left: 236px; top: 629px; }
  .detail-text {
    font-weight: 600;
    font-size: 23px;
    letter-spacing: 0.3px;
    white-space: nowrap;
  }
  .detail-date .detail-text { margin-left: 26px; }
  .detail-time .detail-text { margin-left: 31px; }
  .detail-place .detail-text {
    margin-left: 46px;
    font-size: 11.5px;
    line-height: 16px;
    text-align: center;
    letter-spacing: 0.2px;
  }
  .blurb {
    position: absolute;
    top: 722px; left: 0; width: 851px;
    text-align: center;
    font-style: italic;
    font-weight: 300;
    font-size: 22px;
    line-height: 26.5px;
    white-space: nowrap;
  }
  .closing {
    position: absolute;
    top: 884px; left: 0; width: 904px;
    text-align: center;
    font-size: 17.5px;
    line-height: 24px;
    white-space: nowrap;
  }
  .closing strong { font-weight: 700; }
  .contact-row {
    position: absolute;
    top: 965px; left: 0; width: 851px;
    display: flex;
    justify-content: center;
    align-items: center;
    gap: 34px;
  }
  .contact {
    display: flex;
    align-items: center;
    color: var(--green);
    font-weight: 600;
    font-size: 21px;
    white-space: nowrap;
  }
  .contact-icon {
    width: 38px; height: 38px;
    border-radius: 50%;
    background: var(--green);
    display: flex; align-items: center; justify-content: center;
    margin-right: 12px;
    flex: none;
  }
  .partner {
    position: absolute;
    top: 1038px; left: 0; width: 851px;
    text-align: center;
    font-weight: 600;
    font-size: 24px;
    letter-spacing: 1px;
    color: var(--white);
  }
</style>
</head>
<body>
<main class="invitation">
  <div class="card"><div class="card-inner"></div></div>

  <div class="brand">CORBANT</div>

  <h1 class="headline">YOU’RE INVITED</h1>

  <div class="detail detail-date">
    <svg width="45" height="42" viewBox="0 0 45 42" fill="none" stroke="var(--green)" stroke-width="2">
      <rect x="4" y="6" width="39" height="34" rx="4"/>
      <rect x="1.5" y="4" width="39" height="34" rx="4" fill="var(--ink)"/>
      <line x1="1.5" y1="13" x2="40.5" y2="13"/>
      <line x1="11" y1="1" x2="11" y2="7"/>
      <line x1="31" y1="1" x2="31" y2="7"/>
      <polyline points="13,24 19,30 29,20" stroke-width="2.5" stroke-linecap="round" stroke-linejoin="round"/>
    </svg>
    <span class="detail-text">TUESDAY - OCTOBER 29, 2025</span>
  </div>

  <div class="detail detail-time">
    <svg width="45" height="51" viewBox="0 0 45 51" fill="none" stroke="var(--green)" stroke-width="3">
      <path d="M3 12 A8 8 0 0 1 14 3 Z" fill="var(--green)" stroke-linejoin="round"/>
      <path d="M42 12 A8 8 0 0 0 31 3 Z" fill="var(--green)" stroke-linejoin="round"/>
      <circle cx="22.5" cy="28" r="19"/>
      <polyline points="22.5,16 22.5,29 31,29" stroke-linecap="round"/>
      <line x1="10" y1="44" x2="7" y2="49" stroke-linecap="round"/>
      <line x1="35" y1="44" x2="38" y2="49" stroke-linecap="round"/>
    </svg>
    <span class="detail-text">6:30 PM – 9:30 PM</span>
  </div>

  <div class="detail detail-place">
    <svg width="30" height="36" viewBox="0 0 30 36" fill="none" stroke="var(--green)" stroke-width="1.8">
      <path d="M15 28 C8 19 5 15 5 11 A10 10 0 0 1 25 11 C25 15 22 19 15 28 Z"/>
      <circle cx="15" cy="11" r="4"/>
      <ellipse cx="15" cy="31" rx="13" ry="3.5"/>
    </svg>
    <span class="detail-text">THE GRAND BALLROOM, CITY CONFERENCE CENTER<br>123 BUSINESS AVENUE, SUITE 400</span>
  </div>

  <p class="blurb">Join us for an exclusive evening hosted by Corbant,<br>bringing together valued partners and colleagues<br>for meaningful conversation, insights, and<br>networking.</p>

  <p class="closing">We look forward to seeing you there!<br>For questions or special requests, please <strong>contact:</strong></p>

  <div class="contact-row">
    <div class="contact contact-email">
      <span class="contact-icon">
        <svg width="26" height="26" viewBox="0 0 26 26" fill="none" stroke="var(--white)" stroke-width="1.5">
          <circle cx="13" cy="13" r="11"/>
          <ellipse cx="13" cy="13" rx="5" ry="11"/>
          <line x1="2" y1="13" x2="24" y2="13"/>
          <path d="M4 7 H22 M4 19 H22"/>
        </svg>
      </span>
      <span>events@corbant.com</span>
    </div>

    <div class="contact contact-phone">
      <span class="contact-icon">
        <svg width="24" height="24" viewBox="0 0 24 24" fill="var(--white)">
          <path d="M6.5 2.5 L9.5 7 L7.5 9.5 C8.5 12 11.5 15 14 16 L16.5 14 L21 17 L19 20.5 C12 21 3.5 12.5 3 5 Z"/>
          <path d="M14 3 A7 7 0 0 1 21 10" fill="none" stroke="var(--white)" stroke-width="1.5"/>
          <path d="M14 6.5 A3.5 3.5 0 0 1 17.5 10" fill="none" stroke="var(--white)" stroke-width="1.5"/>
        </svg>
      </span>
      <span>555-010-2486</span>
    </div>
  </div>

  <div class="partner">KELO BRIM TZ</div>
</main>
</body>
</html>
```